Redesign of Business Cards to Update them!

We want a full overhaul of our business cards! We have a design that is almost 5 years old and it needs to be updated to be current

Address is 457 Calloway Court Suite B Fernhaven CA 95317
PH: 5554417382
Tindlebox.com

Hours M-F 10AM-4PM
Sat and Sunday Closed

```html
<!DOCTYPE html>
<html lang="en">
<head>
<meta charset="utf-8">
<title>Tindlebox Business Card</title>
<link rel="stylesheet" href="https://fonts.googleapis.com/css2?family=Baloo+2:wght@500;700;800&display=swap">
<style>
  :root {
    --page-bg: #f1f1f1;
    --card-white: #ffffff;
    --brand-red: #ff0000;
    --ink: #111111;
    --art-soft: #ffd6d6;
  }
  * { margin: 0; padding: 0; box-sizing: border-box; }
  html, body {
    width: 1200px; height: 598px; overflow: hidden;
    background: var(--page-bg);
    font-family: "Baloo 2", "Trebuchet MS", sans-serif;
  }
  .stage { position: relative; width: 1200px; height: 598px; }
  .card {
    position: absolute; top: 153px; width: 461px; height: 282px;
    background: var(--card-white); border-radius: 10px; overflow: hidden;
    box-shadow: 6px 8px 14px rgba(0,0,0,0.28);
  }
  .card--front { left: 120px; }
  .card--back { left: 604px; }

  .front__band { position: absolute; top: 0; height: 218px; background: var(--brand-red); }
  .front__band--left { left: 0; width: 75px; }
  .front__band--right { right: 0; width: 57px; }
  .front__art {
    position: absolute; left: 96px; top: 19px; width: 261px; height: 113px;
    background: linear-gradient(90deg, var(--brand-red) 0%, var(--art-soft) 50%, var(--brand-red) 100%);
    border-radius: 6px;
  }
  .front__name {
    position: absolute; left: 96px; top: 142px; width: 282px;
    font-size: 52px; font-weight: 800; line-height: 1; color: var(--ink);
    text-align: center;
  }
  .front__url {
    position: absolute; left: 0; right: 0; top: 243px;
    text-align: center; font-size: 14px; font-weight: 700; color: var(--ink);
  }

  .back__art {
    position: absolute; left: 50px; top: 38px; width: 119px; height: 51px;
    background: linear-gradient(90deg, var(--brand-red) 0%, var(--art-soft) 50%, var(--brand-red) 100%);
    border-radius: 4px;
  }
  .back__name {
    position: absolute; left: 50px; top: 96px;
    font-size: 28px; font-weight: 800; line-height: 1; color: var(--ink);
  }
  .contact { position: absolute; left: 24px; top: 169px; list-style: none; }
  .contact__item {
    display: flex; align-items: center; gap: 12px; height: 19px;
    font-size: 14px; font-weight: 700; color: var(--ink);
  }
  .contact__icon { width: 16px; height: 16px; flex: none; }
  .back__band {
    position: absolute; left: 0; right: 0; bottom: 0; height: 64px;
    background: var(--brand-red);
  }
  .back__address {
    position: absolute; left: 52px; top: 22px;
    font-size: 14px; font-weight: 700; color: var(--card-white); white-space: nowrap;
  }
</style>
</head>
<body>
<main class="stage">
  <section class="card card--front">
    <div class="front__band front__band--left"></div>
    <div class="front__band front__band--right"></div>
    <div class="front__art" role="img" aria-label="Illustration of a sad character with a broken phone, an arrow, and a happy character with a repaired phone"></div>
    <div class="front__name">Tindlebox</div>
    <div class="front__url">Tindlebox.com</div>
  </section>

  <section class="card card--back">
    <div class="back__art" role="img" aria-label="Small illustration of a character before and after phone repair"></div>
    <div class="back__name">Tindlebox</div>
    <ul class="contact">
      <li class="contact__item">
        <svg class="contact__icon" viewBox="0 0 16 16" aria-hidden="true">
          <circle cx="8" cy="8" r="8" fill="var(--brand-red)"/>
          <path d="M5.3 4.2l1.3 1.9-.8.9c.5 1.1 1.3 1.9 2.4 2.4l.9-.8 1.9 1.3-.7 1.4c-2.9-.3-5.5-2.9-5.8-5.8z" fill="#fff"/>
        </svg>
        5554417382
      </li>
      <li class="contact__item">
        <svg class="contact__icon" viewBox="0 0 16 16" aria-hidden="true">
          <circle cx="8" cy="8" r="8" fill="var(--brand-red)"/>
          <g fill="none" stroke="#fff" stroke-width="1">
            <circle cx="8" cy="8" r="5"/>
            <ellipse cx="8" cy="8" rx="2.2" ry="5"/>
            <line x1="3" y1="8" x2="13" y2="8"/>
          </g>
        </svg>
        Tindlebox.com
      </li>
    </ul>
    <div class="back__band">
      <p class="back__address">457 Calloway Court Suite B Fernhaven CA 95317</p>
    </div>
  </section>
</main>
</body>
</html>
```